Real Estate Investment Company

Design Powerpoint slides are consistent with our logo, colors, and typeface. These Powerpoint slides will be used in all aspects of the business from live presentations to presentation decks available on a website or via email. Need to have different slide types created that allow for different types of slides such as cover pages, text heavy pages, image and chart heavy pages, multiple column pages, and mixed content pages.
Updates

Reason: to give additional time to get the design correct. I plan on making a selection in the next day or 2

Target Market(s)

Real Estate Investors

Industry/Entity Type

Investment

Other font styles liked:
• Consistent with logo

Requirements
Must have
• Our colors
• Our logo where possible
• Different slide designs of the same theme to allow for different types of slides such as cover pages, text heavy, picture heavy, and mixed content.
• Slides in both portrait and landscape orientation
Nice to have

```html
<!DOCTYPE html>
<html lang="en">
<head>
<meta charset="utf-8">
<title>PowerPoint Design Idea – Part 01</title>
<link href="https://fonts.googleapis.com/css2?family=Oswald:wght@300;400;600&family=Cormorant+Garamond:wght@500;600&family=Open+Sans:wght@400;600;700&family=Montserrat:wght@400;700;800&display=swap" rel="stylesheet">
<style>
:root{
  --bg:#000;
  --head:#a9d3e6;
  --navy:#24327a;
  --blue:#1f5fc4;
  --sky:#dcecf4;
  --slate:#4b5a78;
  --ink:#333;
  --muted:#9a9a9a;
  --red:#c8413a;
  --orange:#f39a1d;
  --gold:#e7b93a;
  --green:#8cbd4b;
  --teal:#25a7c7;
  --charcoal:#2b2b2e;
}
*{box-sizing:border-box;margin:0;padding:0}
html,body{width:1200px;height:1200px;overflow:hidden;background:var(--bg)}
body{position:relative;font-family:"Open Sans",sans-serif;color:var(--ink)}
.page-title{position:absolute;top:10px;left:0;width:1175px;text-align:center;font:300 38px "Oswald",sans-serif;letter-spacing:1.5px;color:var(--head)}
.page-sub{position:absolute;left:0;width:1175px;text-align:center;font:300 17px "Oswald",sans-serif;letter-spacing:.5px;color:var(--head)}
.sub1{top:84px}.sub2{top:113px}

.slide{position:absolute;background:#fff}
.inner{position:absolute;inset:5px;overflow:hidden;background:#fff;box-shadow:0 0 3px rgba(0,0,0,.35)}
.c1{left:16px;width:201px}.c2{left:257px;width:199px}.c3{left:490px;width:211px}.c4{left:730px;width:212px}.c5{left:965px;width:211px}
.r1{top:214px;height:118px}.r2{top:342px;height:121px}.r3{top:472px;height:122px}.r4{top:602px;height:121px}.r5{top:738px;height:117px}.r6{top:866px;height:123px}

.abs{position:absolute}
.center{text-align:center;left:0;right:0}
.serif{font-family:"Cormorant Garamond",serif}
.cond{font-family:"Oswald",sans-serif}
.mont{font-family:"Montserrat",sans-serif}
.brand{font:600 5px "Cormorant Garamond",serif;letter-spacing:.6px;color:var(--navy)}
.brand-lg{font-size:7px}
.mark{display:inline-block;width:7px;height:7px;border:1px solid currentColor;vertical-align:middle;margin-right:2px}
.tiny{font-size:3px;line-height:4.2px;color:var(--muted)}
.small{font-size:4px;line-height:5px}
.foot{position:absolute;right:5px;bottom:3px;width:8px;height:4px;border:1px solid var(--navy)}
.photo{position:absolute}
.hd{font:500 8px "Cormorant Garamond",serif;color:var(--navy);letter-spacing:.5px}
.rule{position:absolute;height:1px}
.dot{position:absolute;border-radius:50%}
.bar{position:absolute}
</style>
</head>
<body>

<h1 class="page-title">POWERPOINT DESIGN IDEA (PART-01) [STILL WORKING]</h1>
<p class="page-sub sub1">THIS SUBMISSION CONTAINS OPENER, COVERPAGE, AGENDA, TIMELINE IDEAS ( STILL WORKING ON FORMATING FEW SLIDES)</p>
<p class="page-sub sub2">DESIGNED ON LIGHT BACKGROUND (WHITE) 16:9 FORMAT</p>

<!-- Row 1 -->
<section class="slide c1 r1"><div class="inner">
  <div class="abs center brand" style="top:22px"><span class="mark"></span>GRANITE RIDGE HOLDINGS</div>
  <div class="abs center serif" style="top:40px;font-size:9px;color:var(--navy);letter-spacing:.5px">BUSINESS PRESENTATION</div>
  <div class="abs center tiny" style="top:74px">December 12th 2018</div>
  <div class="bar" style="left:0;right:0;top:82px;height:8px;background:var(--navy)"></div>
  <div class="abs center tiny" style="top:84px;color:#fff">Presented by Team</div>
  <div class="foot"></div>
</div></section>

<section class="slide c2 r1"><div class="inner">
  <div class="photo" role="img" aria-label="Glass office tower photograph" style="left:0;top:0;width:70px;bottom:0;background:linear-gradient(160deg,#c6ccd3,#6f7884 60%,#3f4651)"></div>
  <div class="abs" style="left:70px;right:0;top:0;bottom:0;background:var(--sky)"></div>
  <div class="abs brand" style="left:4px;top:48px;background:rgba(255,255,255,.85);padding:1px 2px">GRANITE RIDGE HOLDINGS</div>
  <div class="abs serif" style="left:90px;top:36px;font-size:9px;line-height:11px;color:var(--navy);text-align:center">BUSINESS<br>PRESENTATION</div>
  <div class="bar" style="left:80px;top:86px;width:55px;height:5px;background:var(--navy)"></div>
  <div class="abs tiny" style="left:82px;top:86px;color:#fff">Presented by Team</div>
  <div class="abs tiny" style="left:82px;top:92px">December 12th 2018</div>
  <div class="foot"></div>
</div></section>

<section class="slide c3 r1"><div class="inner">
  <div class="photo" role="img" aria-label="Dark photograph of a skyscraper at dusk" style="inset:0;background:linear-gradient(180deg,#2a2624,#4a4440 50%,#1d1a19)"></div>
  <div class="abs" style="left:33px;right:33px;top:34px;height:38px;border:1px solid #cfcfcf"></div>
  <div class="abs center serif" style="top:41px;font-size:9px;color:#fff">BUSINESS PRESENTATION</div>
  <div class="abs center tiny" style="top:55px;color:#ddd">Business Subtitle</div>
  <div class="abs center" style="top:63px;font-size:4px;color:var(--orange);letter-spacing:1px">●●●●●●</div>
</div></section>

<section class="slide c4 r1"><div class="inner">
  <div class="photo" role="img" aria-label="City skyline at night reflected in water" style="inset:0;background:linear-gradient(180deg,#07122a 0%,#10203a 55%,#3b2d1a 70%,#1a2a55 85%,#0a0f1e)"></div>
  <div class="abs serif" style="left:32px;top:40px;font-size:8px;color:var(--gold)">BUSINESS PRESENTATION</div>
  <div class="abs serif" style="left:32px;top:50px;font-size:8px;color:#fff">Remaining Title</div>
  <div class="abs tiny" style="left:42px;top:64px;width:120px;color:#ddd">Short text about the fund and its yearly plan for all partners.</div>
  <div class="abs tiny" style="right:30px;top:82px;color:#ddd">Presented by Team</div>
</div></section>

<section class="slide c5 r1"><div class="inner">
  <div class="abs" style="inset:0;background:var(--slate)"></div>
  <div class="abs center brand" style="top:20px;color:#6c7fa8"><span class="mark"></span>GRANITE RIDGE HOLDINGS</div>
  <div class="abs center serif" style="top:44px;font-size:9px;color:#e6e9f0">BUSINESS PRESENTATION</div>
  <div class="abs center" style="top:58px;font-size:0">
    <span style="display:inline-block;width:7px;height:7px;background:#4a6fc4;margin:0 1px"></span><span style="display:inline-block;width:7px;height:7px;background:#e04a4a;margin:0 1px"></span><span style="display:inline-block;width:7px;height:7px;background:#8cbd4b;margin:0 1px"></span><span style="display:inline-block;width:7px;height:7px;background:#b06cc4;margin:0 1px"></span>
  </div>
</div></section>

<!-- Row 2 -->
<section class="slide c1 r2"><div class="inner">
  <div class="abs center brand brand-lg" style="top:30px"><span class="mark"></span>GRANITE RIDGE HOLDINGS</div>
  <div class="bar" style="left:0;right:0;top:72px;height:24px;background:var(--navy)"></div>
  <div class="abs serif" style="left:6px;top:79px;font-size:8.5px;color:#fff">BUSINESS PRESENTATION</div>
  <div class="abs tiny" style="left:148px;top:76px;width:48px;color:#cdd4f0">Yearly review of fund results and goals.</div>
  <div class="foot"></div>
</div></section>

<section class="slide c2 r2"><div class="inner">
  <div class="photo" role="img" aria-label="Pink and purple sunset sky photograph" style="inset:0;background:linear-gradient(160deg,#e23a55,#a3245f 45%,#3a2a6a)"></div>
  <div class="abs center cond" style="top:42px;font-size:10px;font-weight:600;color:#fff">BUSINESS PRESENTATION</div>
  <div class="abs center tiny" style="top:59px;color:#f3d0da">Business Subtitle</div>
  <div class="abs center tiny" style="top:66px;color:#f3d0da">PRESENTED BY: TEAM</div>
</div></section>

<section class="slide c3 r2"><div class="inner">
  <div class="abs center brand brand-lg" style="top:30px"><span class="mark"></span>GRANITE RIDGE HOLDINGS</div>
  <div class="abs center mont" style="top:60px;font-size:5px;font-weight:800;letter-spacing:1px;color:#222">WELCOME</div>
  <div class="abs tiny" style="left:40px;right:40px;top:72px;text-align:center">We build lasting value for every investor through careful property selection and honest reporting.</div>
  <div class="foot"></div>
</div></section>

<section class="slide c4 r2"><div class="inner">
  <div class="abs" style="left:0;right:0;top:0;height:72px;background:#4a6fc4"></div>
  <div class="abs center mont" style="top:24px;font-size:5px;font-weight:800;color:#f2e14a">WELCOME</div>
  <div class="abs tiny" style="left:30px;right:30px;top:33px;text-align:center;color:#e3e9f7">We build lasting value for every investor through careful property selection and honest reporting each year.</div>
  <div class="abs tiny" style="left:20px;right:20px;top:80px;text-align:center">Our team serves investors with clear goals and steady returns.</div>
  <div class="foot"></div>
</div></section>

<section class="slide c5 r2"><div class="inner">
  <div class="abs center serif" style="top:6px;font-size:7px;color:var(--navy)">AGENDA IDEA - 02</div>
  <div class="abs center tiny" style="top:16px">Topics we will cover today in order</div>
  <div class="rule" style="left:12px;right:12px;top:24px;background:linear-gradient(90deg,#2a6dd1,#c8413a,#8cbd4b,#f39a1d,#25a7c7)"></div>
  <div class="abs serif" style="left:12px;right:12px;top:28px;display:flex;justify-content:space-between;font-size:8px">
    <span style="color:#2a6dd1">01</span><span style="color:#c8413a">02</span><span style="color:#8cbd4b">03</span><span style="color:#7a3fb0">04</span><span style="color:#25a7c7">05</span>
  </div>
  <div class="abs tiny" style="left:12px;right:12px;top:40px;display:flex;justify-content:space-between"><span>Intro</span><span>About</span><span>Vision</span><span>Services</span><span>Values</span></div>
  <div class="rule" style="left:12px;right:12px;top:54px;background:linear-gradient(90deg,#25a7c7,#f39a1d,#8cbd4b,#c8413a,#2a6dd1)"></div>
  <div class="abs serif" style="left:12px;right:12px;top:58px;display:flex;justify-content:space-between;font-size:8px">
    <span style="color:#2a6dd1">06</span><span style="color:#c8413a">07</span><span style="color:#c8413a">08</span><span style="color:#8cbd4b">09</span><span style="color:#2a6dd1">10</span>
  </div>
  <div class="abs tiny" style="left:12px;right:12px;top:70px;display:flex;justify-content:space-between"><span>Strategy</span><span>Growth</span><span>Projects</span><span>Risks</span><span>Contact</span></div>
  <div class="foot"></div>
</div></section>

<!-- Row 3 -->
<section class="slide c1 r3"><div class="inner">
  <div class="abs center serif" style="top:8px;font-size:7px;color:var(--navy)">AGENDA IDEA - 03</div>
  <div class="rule" style="left:40px;right:40px;top:18px;background:var(--gold)"></div>
  <div class="abs tiny" style="left:12px;top:26px;width:80px">1 Company Overview<br>Who we are and what we do.<br><br>2 Agenda Title<br>Key points for this part.<br><br>3 Agenda Title<br>Key points for this part.</div>
  <div class="abs tiny" style="left:104px;top:26px;width:80px">4 Company Overview<br>Our history and our team.<br><br>5 Agenda Title<br>Key points for this part.<br><br>6 Agenda Title<br>Key points for this part.</div>
  <div class="foot"></div>
</div></section>

<section class="slide c2 r3"><div class="inner">
  <div class="photo" role="img" aria-label="Skyscraper photographed from below against blue sky" style="left:96px;top:0;right:0;bottom:0;background:linear-gradient(180deg,#aac6e0,#5c6f82 45%,#2b3440)"></div>
  <div class="abs serif" style="left:18px;top:8px;font-size:7px;color:var(--navy)">AGENDA IDEA - 04</div>
  <div class="abs tiny" style="left:6px;top:18px;width:86px">Topics we will cover today</div>
  <div class="dot" style="left:8px;top:38px;width:8px;height:8px;background:var(--navy)"></div>
  <div class="dot" style="left:8px;top:56px;width:8px;height:8px;background:var(--navy)"></div>
  <div class="dot" style="left:8px;top:74px;width:8px;height:8px;background:var(--navy)"></div>
  <div class="dot" style="left:52px;top:38px;width:8px;height:8px;background:var(--navy)"></div>
  <div class="dot" style="left:52px;top:56px;width:8px;height:8px;background:var(--navy)"></div>
  <div class="dot" style="left:52px;top:74px;width:8px;height:8px;background:var(--navy)"></div>
  <div class="abs tiny" style="left:18px;top:38px;line-height:18px">Intro<br>Market<br>Results</div>
  <div class="abs tiny" style="left:62px;top:38px;line-height:18px">About<br>Growth<br>Contact</div>
</div></section>

<section class="slide c3 r3"><div class="inner">
  <div class="abs center serif" style="top:6px;font-size:7px;color:var(--navy)">TIMELINE IDEA - 01</div>
  <div class="abs center tiny" style="top:15px">Key milestones from our first five years</div>
  <svg class="abs" style="left:0;top:0" width="201" height="112" viewBox="0 0 201 112">
    <line x1="20" y1="70" x2="185" y2="70" stroke="#999" stroke-width=".5"/>
    <g font-family="Open Sans" font-size="4" fill="#555" font-weight="700"><text x="30" y="68">2010</text><text x="63" y="68">2011</text><text x="96" y="68">2012</text><text x="129" y="68">2013</text><text x="162" y="68">2014</text></g>
    <circle cx="70" cy="40" r="4" fill="#f39a1d"/><path d="M66 42 L70 50 L74 42Z" fill="#f39a1d"/>
    <circle cx="135" cy="40" r="4" fill="#e0285a"/><path d="M131 42 L135 50 L139 42Z" fill="#e0285a"/>
    <circle cx="37" cy="84" r="4" fill="#4cae4c"/><path d="M33 82 L37 74 L41 82Z" fill="#4cae4c"/>
    <circle cx="103" cy="84" r="4" fill="#f39a1d"/><path d="M99 82 L103 74 L107 82Z" fill="#f39a1d"/>
    <circle cx="168" cy="84" r="4" fill="#8cbd4b"/><path d="M164 82 L168 74 L172 82Z" fill="#8cbd4b"/>
    <g font-family="Open Sans" font-size="3" fill="#999"><text x="77" y="38">First fund</text><text x="142" y="38">New office</text><text x="44" y="85">Founded</text><text x="110" y="85">Expansion</text><text x="175" y="85">Growth</text></g>
  </svg>
  <div class="foot"></div>
</div></section>

<section class="slide c4 r3"><div class="inner">
  <div class="abs center serif" style="top:6px;font-size:7px;color:var(--navy)">TIMELINE IDEA - 02</div>
  <div class="abs center tiny" style="top:15px">Key milestones from our first five years</div>
  <svg class="abs" style="left:0;top:0" width="202" height="112" viewBox="0 0 202 112">
    <g font-family="Open Sans" font-size="3" fill="#999" text-anchor="middle"><text x="46" y="36">Sub heading</text><text x="100" y="36">Sub heading</text><text x="154" y="36">Sub heading</text><text x="46" y="86">Sub heading</text><text x="100" y="86">Sub heading</text><text x="154" y="86">Sub heading</text></g>
    <g>
      <path d="M20 58h25l3 4-3 4H20z" fill="#4b5a78"/><path d="M47 58h25l3 4-3 4H47l3-4z" fill="#2a6dd1"/>
      <path d="M74 58h25l3 4-3 4H74l3-4z" fill="#c8413a"/><path d="M101 58h25l3 4-3 4h-25l3-4z" fill="#7a3fb0"/>
      <path d="M128 58h25l3 4-3 4h-25l3-4z" fill="#25a7c7"/><path d="M155 58h25l3 4-3 4h-25l3-4z" fill="#f39a1d"/>
    </g>
    <g font-family="Open Sans" font-size="4" fill="#fff" text-anchor="middle"><text x="33" y="63.5">2010</text><text x="61" y="63.5">2011</text><text x="88" y="63.5">2012</text><text x="115" y="63.5">2013</text><text x="142" y="63.5">2014</text><text x="169" y="63.5">2015</text></g>
  </svg>
  <div class="foot"></div>
</div></section>

<section class="slide c5 r3"><div class="inner">
  <div class="bar" style="left:80px;top:72px;width:44px;height:6px;background:var(--navy)"></div>
  <div class="abs tiny" style="left:84px;top:73px;color:#fff">Now... lets talk about</div>
  <div class="abs center" style="top:85px;font-size:8px;color:#222">INTRODUCTION</div>
  <div class="rule" style="left:70px;right:70px;top:96px;background:var(--navy)"></div>
  <div class="foot"></div>
</div></section>

<!-- Row 4 -->
<section class="slide c1 r4"><div class="inner">
  <div class="abs tiny" style="left:120px;top:10px;color:var(--red)">CORPORATE SLIDE</div>
  <div class="abs cond" style="left:122px;top:14px;font-size:6px;color:#222">ABOUT US</div>
  <div class="abs tiny" style="left:90px;top:30px;width:96px">Our firm buys, improves and manages homes and offices for long term gain. We share plain reports with every partner and keep costs low.<br><br>We look for steady cash flow, good locations and fair prices in growing towns.</div>
  <div class="abs" style="left:110px;top:84px;font-size:0">
    <span style="display:inline-block;width:7px;height:7px;border-radius:50%;background:#2a6dd1;margin-right:1px"></span><span style="display:inline-block;width:7px;height:7px;border-radius:50%;background:#c8413a;margin-right:1px"></span><span style="display:inline-block;width:7px;height:7px;border-radius:50%;background:#f39a1d;margin-right:1px"></span><span style="display:inline-block;width:7px;height:7px;border-radius:50%;background:#7a3fb0;margin-right:1px"></span><span style="display:inline-block;width:7px;height:7px;border-radius:50%;background:#25a7c7"></span>
  </div>
  <div class="foot"></div>
</div></section>

<section class="slide c2 r4"><div class="inner">
  <div class="abs" style="left:0;right:0;top:0;height:48px;background:#9aaac2"></div>
  <div class="abs center" style="top:12px;font-size:7px;color:#e8edf4">About The Company</div>
  <div class="abs" style="left:0;right:0;top:48px;height:54px;background:#33363c"></div>
  <div class="abs" style="left:18px;top:58px;font-size:7px;line-height:9px;color:#fff">Company<br><span style="color:var(--teal)">Memorabilia</span></div>
  <div class="abs tiny" style="left:18px;top:78px;width:60px;color:#aaa">Our path from one home to a broad portfolio.</div>
  <div class="abs" style="left:106px;top:52px;font-size:5px;color:var(--gold)">2012</div>
  <div class="abs" style="left:150px;top:52px;font-size:5px;color:var(--red)">2014</div>
  <div class="abs" style="left:106px;top:80px;font-size:5px;color:var(--gold)">2013</div>
  <div class="abs" style="left:150px;top:80px;font-size:5px;color:#b06cc4">2015</div>
</div></section>

<section class="slide c3 r4"><div class="inner">
  <div class="abs tiny" style="left:110px;top:10px;color:var(--red)">CORPORATE SLIDE</div>
  <div class="abs cond" style="left:112px;top:14px;font-size:6px;color:#222">ABOUT US</div>
  <div class="abs" style="left:126px;top:32px;width:74px;height:36px;background:#c0393b"></div>
  <div class="abs" style="left:130px;top:34px;font-size:8px;color:#fff;font-family:Georgia,serif">“</div>
  <div class="abs" style="left:145px;top:38px;width:50px;font-size:3.4px;line-height:4px;color:#fff">There are no secrets to success. It is the result of preparation, hard work and learning from failure. – Jordan Ellis</div>
  <div class="abs tiny" style="left:14px;top:78px;width:180px;color:#d4a24a">Text about our work and people. Text about our work and people. Text about our work and people.</div>
  <div class="foot"></div>
</div></section>

<section class="slide c4 r4"><div class="inner">
  <div class="abs" style="left:0;top:0;width:66px;bottom:0;background:var(--green)"></div>
  <div class="abs" style="left:8px;top:30px;font-size:4px;font-weight:700;color:#222">SUMMIT GOAL</div>
  <div class="abs cond" style="left:8px;top:58px;font-size:10px;font-weight:600;color:#fff">BUSINESS</div>
  <div class="abs tiny" style="left:8px;top:74px;width:52px;color:#eef5e3">Short text about our aims for all investors.</div>
  <div class="foot"></div>
</div></section>

<section class="slide c5 r4"><div class="inner">
  <div class="abs" style="left:18px;top:8px;font-size:5.5px;font-weight:700;color:var(--blue)">INVESTMENT OBJECTIVE</div>
  <div class="rule" style="left:18px;right:18px;top:17px;background:#ccc"></div>
  <div class="bar" style="left:24px;right:18px;top:22px;height:9px;background:var(--blue)"></div>
  <div class="abs" style="left:28px;top:24px;font-size:3.4px;color:#fff;font-weight:700">Profit from inefficiencies in equity and index options markets.</div>
  <div class="abs" style="left:44px;top:36px;font-size:3px;line-height:5px;color:#222">➤ Buy options that are underpriced<br>➤ Sell options that are overpriced</div>
  <div class="bar" style="left:24px;right:18px;top:60px;height:14px;background:var(--blue)"></div>
  <div class="abs" style="left:28px;top:62px;width:150px;font-size:3.2px;line-height:4px;color:#fff;font-weight:700">Achieve outsized and consistent returns by keeping a small and nimble fund that moves in and out of trades quickly.</div>
  <div class="abs tiny" style="left:18px;bottom:6px;color:#444">MARLOW</div>
  <div class="abs tiny" style="right:18px;bottom:6px">Marlow Derivatives Fund</div>
</div></section>

<!-- Row 5 -->
<section class="slide c1 r5"><div class="inner">
  <div class="abs" style="left:8px;top:8px;font-size:5.5px;font-weight:700;color:var(--blue)">INVESTMENT STRATEGY</div>
  <div class="bar" style="left:10px;right:10px;top:18px;height:12px;background:var(--blue)"></div>
  <div class="abs" style="left:13px;top:20px;width:160px;font-size:3.2px;line-height:4px;color:#fff;font-weight:700">Strategy derived from a dynamic optimisation problem that maximises returns within a given risk limit.</div>
  <div class="bar" style="left:20px;top:33px;width:70px;height:5px;background:#f2e14a"></div>
  <div class="bar" style="left:94px;top:33px;width:78px;height:5px;background:#f2e14a"></div>
  <div class="abs" style="left:27px;top:34px;font-size:3px;font-weight:700">Parameters / assumptions</div>
  <div class="abs" style="left:98px;top:34px;font-size:3px;font-weight:700">Solution – optimal rules</div>
  <div class="abs" style="left:14px;top:40px;width:78px;height:24px;border:.5px solid #999"></div>
  <div class="abs" style="left:94px;top:40px;width:80px;height:24px;border:.5px solid #999"></div>
  <div class="abs" style="left:18px;top:43px;font-size:3px;line-height:5px">• Assume liquid markets<br>• Assume a price discount</div>
  <div class="abs" style="left:98px;top:43px;font-size:3px;line-height:5px">• When to buy or sell<br>• Which contracts to trade<br>• How many contracts</div>
  <div class="bar" style="left:10px;right:10px;top:68px;height:12px;background:var(--blue)"></div>
  <div class="abs" style="left:13px;top:70px;width:160px;font-size:3.2px;line-height:4px;color:#fff;font-weight:700">We make trades based on these solutions while hitting the price discount offered by the market.</div>
  <div class="abs tiny" style="left:14px;bottom:4px;color:#444">MARLOW</div>
  <div class="abs tiny" style="right:14px;bottom:4px">Marlow Derivatives Fund</div>
</div></section>

<section class="slide c2 r5"><div class="inner">
  <div class="abs" style="left:10px;top:8px;font-size:5.5px;font-weight:700;color:var(--blue)">RISK MANAGEMENT</div>
  <div class="abs" style="left:10px;top:18px;width:92px;height:36px;background:#1d3d7a"></div>
  <div class="abs" style="left:102px;top:18px;width:76px;height:36px;background:var(--orange)"></div>
  <div class="abs" style="left:10px;top:54px;width:92px;height:36px;background:var(--orange)"></div>
  <div class="abs" style="left:102px;top:54px;width:76px;height:36px;background:#d41c1c"></div>
  <div class="dot" style="left:88px;top:42px;width:26px;height:26px;background:#fff"></div>
  <div class="abs" style="left:91px;top:52px;width:20px;text-align:center;font-size:3px;font-weight:700">RISK MGMT</div>
  <div class="abs" style="left:22px;top:30px;font-size:3px;color:#fff">Our top priority is safety</div>
  <div class="abs" style="left:118px;top:24px;width:56px;font-size:3px;line-height:4px;color:#fff">We set tight trade sizes and keep enough cash to stay calm.</div>
  <div class="abs" style="left:20px;top:68px;width:70px;font-size:3px;line-height:4px;color:#fff">We only trade in liquid markets.</div>
  <div class="abs" style="left:118px;top:60px;width:56px;font-size:3px;line-height:4px;color:#fff">The worst drawdown is smaller than the long-run average gain.</div>
  <div class="abs tiny" style="left:14px;bottom:4px;color:#444">MARLOW</div>
  <div class="abs tiny" style="right:14px;bottom:4px">Marlow Derivatives Fund</div>
</div></section>

<section class="slide c3 r5"><div class="inner">
  <div class="abs" style="left:14px;top:8px;font-size:5.5px;font-weight:700;color:var(--blue)">WHY INVEST ?</div>
  <div class="bar" style="left:18px;right:24px;top:18px;height:6px;background:var(--blue)"></div>
  <div class="abs" style="left:21px;top:19px;font-size:3.2px;color:#fff;font-weight:700">Marlow Derivatives Fund, LP offers:</div>
  <div class="abs" style="left:36px;top:29px;font-size:3px;line-height:5.2px;color:#222">➤ A large return potential<br>➤ Low risk over a 3 to 5 year horizon<br>➤ High liquidity with no lockup period<br>➤ A low minimum investment<br>➤ Transparent investment return properties<br>➤ Returns that do not move with stock and bond markets<br>➤ Diversification that lowers overall portfolio risk<br>➤ A small, agile fund that can earn returns big funds cannot</div>
  <div class="abs tiny" style="left:14px;bottom:4px;color:#444">MARLOW</div>
  <div class="abs tiny" style="right:14px;bottom:4px">Marlow Derivatives Fund</div>
</div></section>

<section class="slide c4 r5"><div class="inner">
  <div class="abs" style="left:0;top:0;width:95px;bottom:0;background:#000"></div>
  <div class="dot" style="left:88px;top:48px;width:12px;height:12px;background:#555"></div>
  <div class="dot" style="left:92px;top:52px;width:4px;height:4px;background:#fff"></div>
  <div class="abs tiny" style="left:107px;top:72px;color:#666">Now... Lets talk about</div>
  <div class="abs mont" style="left:107px;top:81px;font-size:5.5px;line-height:7px;font-weight:800;color:#222">INTRODUCTION<br>ABOUT US</div>
  <div class="foot"></div>
</div></section>

<section class="slide c5 r5"><div class="inner">
  <div class="abs" style="left:0;right:0;top:0;height:60px;background:var(--slate)"></div>
  <div class="abs center tiny" style="top:16px;color:#c9d1e0">Now... Let's talk about</div>
  <div class="abs center mont" style="top:36px;font-size:6px;line-height:7px;font-weight:800;color:#fff">GREAT<br>PORTFOLIOS</div>
  <div class="dot" style="left:95px;top:60px;width:12px;height:12px;background:#37465f;border:1.5px solid #fff"></div>
  <div class="foot"></div>
</div></section>

<!-- Row 6 -->
<section class="slide c1 r6"><div class="inner">
  <div class="abs" style="inset:0;background:#a4a4a4"></div>
  <svg class="abs" style="left:0;top:0" width="191" height="113" viewBox="0 0 191 113">
    <path d="M100 42 L191 44 L191 80 L106 82 L100 75 Z" fill="#f39a1d"/>
    <path d="M95 50 L120 48 L116 66 L90 68 Z" fill="#f6b15a"/>
    <rect x="98" y="55" width="9" height="9" fill="#1d3d7a"/>
  </svg>
  <div class="abs" style="left:122px;top:52px;font-size:4px;line-height:5px;color:#fff">Services &amp;<br>Maintenance</div>
  <div class="abs tiny" style="left:150px;top:52px;width:38px;color:#ffe5c2">Care for every property we own.</div>
</div></section>

<section class="slide c2 r6"><div class="inner">
  <div class="abs" style="left:0;top:0;width:122px;bottom:0;background:#4a7fd1"></div>
  <div class="abs" style="left:104px;top:46px;width:28px;height:28px;background:#1e58b8"></div>
  <div class="abs" style="left:60px;top:56px;font-size:5px;line-height:6px;font-weight:700;color:#7ee0ff;text-align:right;letter-spacing:.5px">Business.<br>PROPOSAL.</div>
  <div class="abs tiny" style="left:24px;top:92px;color:#dfe9fb">We look forward to your trust in our team</div>
  <div class="abs" style="left:176px;top:6px;width:8px;height:8px;background:#222"></div>
  <div class="abs tiny" style="left:150px;top:54px;color:#666">Contact: Jane Doe<br>Office: Main Street<br>City Center</div>
</div></section>

<section class="slide c3 r6"><div class="inner">
  <div class="abs" style="left:0;top:0;width:92px;bottom:0;background:var(--charcoal)"></div>
  <div class="abs" style="left:16px;top:16px;font-size:4px;font-weight:700;color:#fff">PARAGRAPH STYLES</div>
  <div class="abs" style="left:30px;top:30px;font-size:0">
    <span style="display:block;width:6px;height:6px;border:1px solid var(--teal);margin-bottom:8px"></span><span style="display:block;width:6px;height:6px;border:1px solid var(--teal);margin-bottom:8px"></span><span style="display:block;width:6px;height:6px;border:1px solid var(--teal);margin-bottom:8px"></span><span style="display:block;width:6px;height:6px;border:1px solid var(--teal);margin-bottom:8px"></span><span style="display:block;width:6px;height:6px;border:1px solid var(--teal)"></span>
  </div>
  <div class="abs tiny" style="left:40px;top:30px;width:48px;color:#888;line-height:4px">Short text about this point here.<br><br>Short text about this point here.<br><br>Short text about this point here.<br><br>Short text about this point here.</div>
  <div class="abs" style="left:102px;top:30px;font-size:0">
    <span style="display:block;width:6px;height:6px;border:1px solid var(--teal);margin-bottom:8px"></span><span style="display:block;width:6px;height:6px;border:1px solid var(--teal);margin-bottom:8px"></span><span style="display:block;width:6px;height:6px;border:1px solid var(--teal);margin-bottom:8px"></span><span style="display:block;width:6px;height:6px;border:1px solid var(--teal)"></span>
  </div>
  <div class="abs tiny" style="left:112px;top:30px;width:80px;line-height:4px">Short text about this point here.<br><br>Short text about this point here.<br><br>Short text about this point here.<br><br>Short text about this point here.</div>
  <div class="foot"></div>
</div></section>

<section class="slide c4 r6"><div class="inner">
  <div class="abs center" style="top:4px;font-size:5px;color:#333">Who We Are</div>
  <div class="abs center tiny" style="top:10px">Here's a few fun facts about our team</div>
  <div class="photo" role="img" aria-label="City skyline photograph with tall buildings" style="left:16px;top:28px;width:70px;height:50px;background:linear-gradient(180deg,#8fb2d6,#6c7a88 55%,#3d4a55)"></div>
  <div class="abs" style="left:110px;top:20px;font-size:3.5px;color:#555">We're a Digital Marketing Startup</div>
  <div class="abs tiny" style="left:110px;top:26px;width:80px">Our crew works on smart ways to reach new buyers.</div>
  <div class="bar" style="left:140px;top:54px;width:40px;height:3px;background:#f2a7a7"></div><div class="bar" style="left:140px;top:54px;width:24px;height:3px;background:var(--blue)"></div>
  <div class="bar" style="left:140px;top:62px;width:40px;height:3px;background:#f2a7a7"></div><div class="bar" style="left:140px;top:62px;width:30px;height:3px;background:var(--blue)"></div>
  <div class="bar" style="left:140px;top:70px;width:40px;height:3px;background:#f2a7a7"></div><div class="bar" style="left:140px;top:70px;width:18px;height:3px;background:var(--blue)"></div>
  <div class="bar" style="left:140px;top:78px;width:40px;height:3px;background:#f2a7a7"></div><div class="bar" style="left:140px;top:78px;width:34px;height:3px;background:var(--blue)"></div>
  <div class="abs tiny" style="left:116px;top:53px;line-height:8px">Lunch<br>Coffee<br>Time<br>Code</div>
  <div class="abs tiny" style="left:16px;top:82px;width:80px;text-align:center">We love what we do every day</div>
</div></section>

<section class="slide c5 r6"><div class="inner">
  <div class="abs center mont" style="top:18px;font-size:6px;font-weight:800;color:#222">ORGANIZATION</div>
  <div class="abs center tiny" style="top:28px">How our team is set up to serve you well</div>
  <svg class="abs" style="left:0;top:0" width="201" height="113" viewBox="0 0 201 113">
    <rect x="100" y="52" width="2" height="4" fill="#2a6dd1"/>
    <rect x="80" y="75" width="2" height="4" fill="#2a6dd1"/>
    <rect x="118" y="75" width="2" height="4" fill="#f39a1d"/>
    <rect x="38" y="96" width="2" height="4" fill="#2a6dd1"/>
    <rect x="90" y="96" width="2" height="4" fill="#2a6dd1"/>
    <rect x="138" y="96" width="2" height="4" fill="#2a6dd1"/>
    <g font-family="Open Sans" font-size="2.6" fill="#555"><text x="104" y="55">CEO</text><text x="84" y="78">CFO</text><text x="122" y="78">COO</text><text x="42" y="99">Sales</text><text x="94" y="99">Legal</text><text x="142" y="99">Ops</text></g>
  </svg>
  <div class="foot"></div>
</div></section>

</body>
</html>
```